Poster Design for a tea beverage brand - seasonal product "Lychee Rose Tea"

We're chain of bubble tea beverage stores, located mainly in New York, and we're looking for professional poster design for our new seasonal product - Lychee Rose Tea(Please note there's no boba in this product). Our brand spirit is to deliver the most authentic flavor of tea from Taiwan. We want the style of the poster to be lovely and energetic that targets at customers around 18-35 age group, both male and female. We would like to see an image of spring felling, expressing the freshness and tasty of our products. Attached are some posters, whose styles are similar to what we want. Also attached our current product photo and some similar product photos downloaded from website for your reference.

```html
<!DOCTYPE html>
<html lang="en">
<head>
<meta charset="utf-8">
<title>Lychee Rose Tea – Seasonal Poster</title>
<link rel="stylesheet" href="https://fonts.googleapis.com/css2?family=Questrial&family=Pacifico&display=swap">
<style>
  :root {
    --sky-red: #f4221a;
    --sunset-orange: #fb7a12;
    --sun-yellow: #fdf21a;
    --lime: #b6ec3a;
    --leaf: #4fba2c;
    --steel: #3d3f44;
    --steel-light: #8a8c90;
    --script-green: #6bb140;
    --white: #ffffff;
    --tea-amber: #e9a62a;
    --tea-gold: #f7c548;
  }
  html, body {
    margin: 0;
    padding: 0;
    width: 900px;
    height: 1200px;
    overflow: hidden;
  }
  .poster {
    position: relative;
    width: 900px;
    height: 1200px;
    overflow: hidden;
    background: linear-gradient(180deg,
      var(--sky-red) 0%,
      var(--sunset-orange) 22%,
      var(--sun-yellow) 50%,
      var(--lime) 66%,
      var(--leaf) 100%);
  }
  .texture {
    position: absolute;
    inset: 0;
    background:
      radial-gradient(ellipse 60% 30% at 20% 15%, rgba(255,160,40,0.35), transparent 70%),
      radial-gradient(ellipse 50% 25% at 80% 80%, rgba(60,170,40,0.35), transparent 70%),
      radial-gradient(ellipse 40% 20% at 30% 85%, rgba(200,240,90,0.3), transparent 70%);
  }
  .headline {
    position: absolute;
    inset: 0;
    width: 900px;
    height: 1200px;
  }
  .headline .flavor,
  .headline .echo,
  .headline .tea-word {
    font-family: "Questrial", "Century Gothic", sans-serif;
  }
  .headline .flavor {
    fill: var(--steel);
    stroke: var(--steel-light);
    stroke-width: 2;
  }
  .headline .echo {
    fill: var(--steel);
  }
  .headline .variety {
    font-family: "Pacifico", cursive;
    fill: var(--script-green);
    stroke: var(--white);
    stroke-width: 10;
    paint-order: stroke;
  }
  .headline .tea-word {
    fill: var(--white);
  }
  .product-glow {
    position: absolute;
    left: 240px;
    top: 720px;
    width: 430px;
    height: 470px;
    border-radius: 50%;
    background: radial-gradient(ellipse at center, rgba(255,255,255,0.9) 30%, rgba(255,255,255,0) 70%);
  }
  .product-photo {
    position: absolute;
    left: 295px;
    top: 760px;
    width: 322px;
    height: 382px;
  }
</style>
</head>
<body>
  <main class="poster">
    <div class="texture" role="img" aria-label="Painterly brush texture in warm sunset and spring green tones"></div>

    <svg class="headline" viewBox="0 0 900 1200" aria-label="Lychee Rose Tea">
      <defs>
        <filter id="lift" x="-10%" y="-10%" width="120%" height="130%">
          <feDropShadow dx="3" dy="4" stdDeviation="3" flood-color="#000" flood-opacity="0.35"/>
        </filter>
        <filter id="soft-lift" x="-10%" y="-10%" width="120%" height="130%">
          <feDropShadow dx="2" dy="3" stdDeviation="4" flood-color="#8a6a00" flood-opacity="0.35"/>
        </filter>
      </defs>

      <text class="echo" x="150" y="380" font-size="190" textLength="560" lengthAdjust="spacingAndGlyphs" opacity="0.45">LYCHEE</text>
      <text class="echo" x="150" y="510" font-size="190" textLength="560" lengthAdjust="spacingAndGlyphs" opacity="0.28">LYCHEE</text>
      <text class="echo" x="150" y="640" font-size="190" textLength="560" lengthAdjust="spacingAndGlyphs" opacity="0.18">LYCHEE</text>
      <text class="echo" x="150" y="770" font-size="190" textLength="560" lengthAdjust="spacingAndGlyphs" opacity="0.1">LYCHEE</text>

      <text class="flavor" x="150" y="240" font-size="190" textLength="560" lengthAdjust="spacingAndGlyphs" filter="url(#lift)">LYCHEE</text>

      <text class="variety" x="345" y="395" font-size="150" filter="url(#lift)">Rose</text>

      <text class="tea-word" x="238" y="650" font-size="330" filter="url(#soft-lift)">Tea</text>
    </svg>

    <div class="product-glow"></div>
    <svg class="product-photo" viewBox="0 0 322 382" role="img" aria-label="Photo of an iced Lychee Rose Tea in a clear plastic cup">
      <defs>
        <linearGradient id="tea-fill" x1="0" y1="0" x2="0" y2="1">
          <stop offset="0" stop-color="#f3e6c4"/>
          <stop offset="0.18" stop-color="var(--tea-gold)"/>
          <stop offset="1" stop-color="var(--tea-amber)"/>
        </linearGradient>
      </defs>
      <path d="M8 22 Q161 -6 314 22 L268 370 Q161 388 54 370 Z" fill="url(#tea-fill)"/>
    </svg>
  </main>
</body>
</html>
```